Corporate Two Sided Business Card

Looking for a Corporate "edgy" Modern look and feel for a business card

We are looking at two options. Dark background with our logo on it, white background with our logo on it - The background is more - Charcoal / Graphite then black

Details will be

Danielle Forsk

Licensee / Director

m. 0428 519 064

e. danielle@quorvela.com.au

quorvela.com.au

Target Market(s)

Professional Business people that refer use business and clients that own Investment Properties

Industry/Entity Type

Business

Contact Information for Business Card

Details will be

Danielle Forsk

Licensee / Director

m. 0428 519 064

quorvela.com.au

Font styles to use
Serif

Colors
000000
ec1f27
eeeeee
ffffff

Requirements
Must have
• Two options - White Background and Dark Background. - Two sided
Nice to have
• A design that is edgy, modern and new to look instead of boring style corporate cards - It should be a full integrated design
Should not have
• Block looking - Cheap.

```html
<!DOCTYPE html>
<html lang="en">
<head>
<meta charset="utf-8">
<title>Quorvela Business Card</title>
<link href="https://fonts.googleapis.com/css2?family=Montserrat:wght@500;600;700&family=Didact+Gothic&display=swap" rel="stylesheet">
<style>
  :root {
    --page: #e6e6e6;
    --graphite-light: #7d7e7f;
    --graphite-mid: #5a5b5d;
    --graphite-dark: #3b3c3e;
    --red: #ec1f27;
    --white: #ffffff;
    --ink: #0d0d0e;
  }
  * { margin: 0; padding: 0; box-sizing: border-box; }
  html, body {
    width: 1200px; height: 568px; overflow: hidden;
    background: var(--page);
  }
  .stage { position: relative; width: 1200px; height: 568px; }
  .card {
    position: absolute; top: 157px;
    width: 422px; height: 254px;
    background: linear-gradient(205deg, var(--graphite-light) 0%, var(--graphite-mid) 45%, var(--graphite-dark) 100%);
    overflow: hidden;
  }
  .card--front { left: 161px; }
  .card--back { left: 617px; }

  .brand {
    position: absolute; left: 21px; top: 28px;
    display: flex; align-items: center; gap: 8px;
  }
  .brand__mark { width: 18px; height: 18px; background: var(--red); }
  .brand__name {
    font-family: "Montserrat", sans-serif; font-weight: 600;
    font-size: 30px; line-height: 1; color: var(--white); letter-spacing: 0.2px;
  }

  .person { position: absolute; left: 21px; top: 131px; }
  .person__name {
    font-family: "Montserrat", sans-serif; font-weight: 700;
    font-size: 16px; color: var(--red); line-height: 1.2;
  }
  .person__role {
    font-family: "Didact Gothic", sans-serif;
    font-size: 9.5px; color: var(--white); margin-top: 1px;
  }

  .contacts { position: absolute; left: 21px; top: 183px; list-style: none; }
  .contacts__item {
    display: flex; align-items: center; height: 15.5px;
    font-family: "Didact Gothic", sans-serif; font-size: 11.5px; color: var(--white);
  }
  .contacts__icon { width: 8px; height: 8px; margin: 0 11px 0 5px; fill: var(--red); }

  .back-brand {
    position: absolute; inset: 0;
    display: flex; align-items: center; justify-content: center; gap: 10px;
  }
  .back-brand__mark { width: 22px; height: 22px; background: var(--ink); }
  .back-brand__name {
    font-family: "Montserrat", sans-serif; font-weight: 600;
    font-size: 40px; color: var(--ink); line-height: 1;
  }
</style>
</head>
<body>
<main class="stage">
  <section class="card card--front">
    <div class="brand">
      <span class="brand__mark"></span>
      <span class="brand__name">quorvela</span>
    </div>
    <div class="person">
      <p class="person__name">Danielle Forsk</p>
      <p class="person__role">Licensee / Director</p>
    </div>
    <ul class="contacts">
      <li class="contacts__item">
        <svg class="contacts__icon" viewBox="0 0 10 10"><path d="M2 0.5 L3.8 2.6 L2.8 3.6 Q4 6 6.4 7.2 L7.4 6.2 L9.5 8 L8.2 9.5 Q1.5 8.5 0.5 1.8 Z"/></svg>
        0428 519 064
      </li>
      <li class="contacts__item">
        <svg class="contacts__icon" viewBox="0 0 10 10"><path d="M0 2 H10 V8.5 H0 Z M0.6 2.4 L5 5.6 L9.4 2.4" stroke="#5a5b5d" stroke-width="0.8"/></svg>
        danielle@quorvela.com.au
      </li>
      <li class="contacts__item">
        <svg class="contacts__icon" viewBox="0 0 10 10"><circle cx="5" cy="5" r="4.6"/><path d="M0.5 5 H9.5 M5 0.5 Q2.5 5 5 9.5 M5 0.5 Q7.5 5 5 9.5" stroke="#5a5b5d" stroke-width="0.7" fill="none"/></svg>
        www.quorvela.com.au
      </li>
    </ul>
  </section>

  <section class="card card--back">
    <div class="back-brand">
      <span class="back-brand__mark"></span>
      <span class="back-brand__name">quorvela</span>
    </div>
  </section>
</main>
</body>
</html>
```